Cool Landing page with email address sign up (mockups provided)

I need a landing page for a service that will send a weekly email to people who are looking for jobs in startups. On the landing page there is a call to action (submit button) to register their email address. The service is called VentureCrew and it is a side project to try to assist startup companies with hiring people.

I just want one single form field "Email".

The feeling I want to give people is one of adventure. Imagine the person is living in Gdansk Poland, they are a technical/IT expert and have dreams of making it big in a Startup in London. This is his big chance, this is going to allow him to do it! He's signing up to a big promise! It should be cool, professional, exciting.

A major influence should be:
http://brassteapotcorner.com/

There should also be a call to tweet in a cool way like on (http://www.withinfoundry.org/).

Look at this - taking a leap of faith, like this:
http://kitebloomapp.com/wp-content/uploads/2011/09/19.jpg

This is super with the colours - striking!:
http://pelvora.org/

Fly your kit higher!:
http://tobiasvrenn.com/

If necessary use sex to sell:
http://kitebloomapp.com/wp-content/uploads/2011/09/24.jpg

Some original art would work:
http://kitebloomapp.com/wp-content/uploads/2011/09/fx_ss_group1_sm_filtered_0000s_0007_Layer-14.jpg

This is effective for a call to action, I'm looking to you to act!:
http://kitebloomapp.com/wp-content/uploads/2011/09/weblance.jpg
Take inspiration from:
http://www.withinfoundry.org/
http://venturecrew.org/
http://quarrymint.com/

***N.B.: I would prefer original art background over a photo

Also:
http://pixelfolioroom.com/inspiration/a-showcase-of-landing-pages-designed-for-conversion
especially:
http://pixelfolioroom.com/wp-content/uploads/2011/09/01-landing.jpg
http://pixelfolioroom.com/wp-content/uploads/2011/09/04-landing.jpg
http://pixelfolioroom.com/wp-content/uploads/2011/10/texture21.jpg

I really like the colouring from Tinker Ledger:
http://board.quillmatic.com/

Reason: I'm going to be away for a few days so I won't have enough time to properly provide feedback.

The payment is now guaranteed. This project is a single page only.

I've added a few more example landing pages that I like.

I've now added the venturecrew logo image that should be used.

I've updated brief with more examples of what I'm looking for

Reason: I'm still progressing with candidate designs.

Target Market(s)

Technical people, english not being their native language. Ambitious to work in London/Dublin in a tech startup company. They want to receive a weekly emails with startup jobs in london or dublin.

Requirements
Must have
• Eyes must be drawn to the email registration form to get them to submit their email address. The background image or website theme should encourage their desires to work in the big city in exciting startup companies.

Should have a prompt to tweet (once pressed I'll do my own popup)

```html
<!DOCTYPE html>
<html lang="en">
<head>
<meta charset="utf-8">
<title>VentureCrew — Are you a Starter?</title>
<link rel="stylesheet" href="https://fonts.googleapis.com/css2?family=PT+Sans+Narrow:wght@400;700&display=swap">
<style>
  :root {
    --sky-top: #8d9cc4;
    --sky-mid: #c9b79a;
    --city: #a88a62;
    --water: #7f8da6;
    --water-low: #9aa4b6;
    --frame: rgba(60, 60, 60, 0.85);
    --panel: #000000;
    --panel-head: #2a2a2a;
    --gold: #e8c455;
    --gold-deep: #c99a2a;
    --white: #ffffff;
    --field: #f2f2f2;
    --field-text: #b5b5b5;
    --ink: #111111;
    --tag: #efe7cf;
    --tag-accent: #1f9fd6;
    --bird: #5fc2ee;
  }
  * { box-sizing: border-box; margin: 0; padding: 0; }
  html, body { width: 1200px; height: 675px; overflow: hidden; }
  body {
    position: relative;
    font-family: "PT Sans Narrow", "Arial Narrow", sans-serif;
    font-weight: 700;
    color: var(--white);
  }
  .city-backdrop {
    position: absolute; inset: 0;
    background: linear-gradient(180deg,
      var(--sky-top) 0%, #aab0c4 18%, var(--sky-mid) 32%,
      var(--city) 45%, #7d6a52 56%, var(--water) 62%,
      #b39a72 74%, var(--water-low) 100%);
  }
  .signup-frame {
    position: absolute; left: 432px; top: 160px;
    width: 336px; height: 355px;
    background: var(--frame);
    border-radius: 4px;
  }
  .signup-panel {
    position: absolute; left: 440px; top: 168px;
    width: 320px; height: 339px;
    background: var(--panel);
    border-radius: 3px;
    overflow: hidden;
  }
  .panel-head {
    position: absolute; left: -40px; top: -60px;
    width: 400px; height: 130px;
    background: linear-gradient(180deg, var(--panel-head), #111);
    border-radius: 0 0 50% 50% / 0 0 30% 30%;
  }
  .brand {
    position: absolute; left: 0; right: 0; top: 10px;
    text-align: center;
    font-size: 47px; line-height: 1;
    color: var(--gold);
    letter-spacing: -0.5px;
  }
  .prompt {
    position: absolute; left: 0; right: 0; top: 82px;
    text-align: center; font-size: 25px; line-height: 1;
  }
  .prompt-echo {
    position: absolute; left: 0; right: 0; top: 108px;
    text-align: center; font-size: 25px; line-height: 1;
    transform: scaleY(-0.6);
    opacity: 0.25;
  }
  .pitch {
    position: absolute; left: 17px; right: 14px;
    font-size: 18.5px; line-height: 20px;
  }
  .pitch-one { top: 145px; }
  .pitch-two { top: 200px; }
  .email-field {
    position: absolute; left: 22px; top: 258px;
    width: 277px; height: 35px;
    border: none; border-radius: 18px;
    background: linear-gradient(180deg, var(--white), var(--field));
    padding: 0 14px;
    font: 700 13.5px "PT Sans Narrow", sans-serif;
    color: var(--ink);
  }
  .email-field::placeholder { color: var(--field-text); }
  .submit-button {
    position: absolute; left: 101px; top: 308px;
    width: 120px; height: 32px;
    border: none; border-radius: 60px 60px 0 0 / 32px 32px 0 0;
    background: linear-gradient(180deg, var(--gold), var(--gold-deep));
    font: 700 19px "PT Sans Narrow", sans-serif;
    color: var(--ink);
    padding-top: 4px;
  }
  .tweet-prompt {
    position: absolute; left: 553px; top: 582px;
    width: 110px; height: 40px;
  }
  .copyright {
    position: absolute; left: 0; right: 0; top: 640px;
    text-align: center; font-size: 12px;
  }
</style>
</head>
<body>
  <div class="city-backdrop" role="img" aria-label="Photograph of a big-city skyline at sunset reflected in a calm river"></div>

  <div class="signup-frame"></div>
  <form class="signup-panel">
    <div class="panel-head"></div>
    <h1 class="brand">VentureCrew</h1>
    <p class="prompt">Are you a Starter?</p>
    <p class="prompt-echo" aria-hidden="true">Are you a Starter?</p>
    <p class="pitch pitch-one">Have skills and need a best companies to choose?</p>
    <p class="pitch pitch-two">Register Now and We help you to make your decision.</p>
    <input class="email-field" type="email" placeholder="Enter Your Email Address...">
    <button class="submit-button" type="submit">Submit</button>
  </form>

  <svg class="tweet-prompt" viewBox="0 0 110 40" aria-label="Follow me">
    <g transform="rotate(-8 60 20)">
      <rect x="22" y="6" width="84" height="24" rx="2" fill="var(--tag)"/>
      <text x="30" y="24" font-family="PT Sans Narrow, sans-serif" font-weight="700" font-size="16" fill="#111">Follow</text>
      <text x="72" y="24" font-family="PT Sans Narrow, sans-serif" font-weight="700" font-size="16" fill="var(--tag-accent)">me!</text>
    </g>
    <circle cx="14" cy="28" r="10" fill="var(--bird)"/>
  </svg>

  <p class="copyright">Copyright © 2011 VentureCrew | All Rights Reserved</p>
</body>
</html>
```